Business Card Design Project

Use our current logo. Clean design.

Industry/Entity Type

Business

Requirements
Must have
• Marisela DUBRANCQ
M. Law
Managing Partner

Alpenvorsa AG
Kornhalmweg 214
CH-3097 Liebefeld

M. +41 79 412 56 27
T. +41 31 928 44 10
F. +41 31 928 44 19

m.dubrancq@alpenvorsa-example.com
www.alpenvorsa-example.com

```html
<!DOCTYPE html>
<html lang="en">
<head>
<meta charset="utf-8">
<title>Alpenvorsa AG – Business Card</title>
<link href="https://fonts.googleapis.com/css2?family=Jost:wght@400;500;700&family=Montserrat:wght@800&display=swap" rel="stylesheet">
<style>
  :root {
    --backdrop: #e9e6e1;
    --card: #ffffff;
    --band: #efefef;
    --ink: #1c1c1c;
    --ink-soft: #3a3a3a;
    --rule: #2a2a2a;
    --shadow: rgba(0, 0, 0, 0.18);
  }
  * { margin: 0; padding: 0; box-sizing: border-box; }
  html, body {
    width: 1200px; height: 900px; overflow: hidden;
    background: var(--backdrop);
    font-family: "Jost", sans-serif;
    color: var(--ink);
  }
  .stage {
    position: relative; width: 1200px; height: 900px;
  }
  .card {
    position: absolute; width: 540px; height: 350px;
    background: var(--card);
    box-shadow: 0 14px 30px var(--shadow);
    overflow: hidden;
  }
  .card--back { left: 40px; top: 275px; }
  .card--front { left: 620px; top: 275px; }

  /* back side */
  .brand {
    position: absolute; left: 0; right: 0; top: 92px;
    display: flex; flex-direction: column; align-items: center;
  }
  .brand__name {
    font-weight: 500; font-size: 34px; letter-spacing: 4px;
    text-transform: uppercase; color: var(--ink);
  }
  .brand__rule {
    width: 200px; height: 1px; background: var(--rule); margin-top: 10px;
  }
  .card--back .contact-email {
    position: absolute; left: 0; right: 0; bottom: 64px;
    text-align: center; font-size: 18px; letter-spacing: 1px;
    text-transform: uppercase; color: var(--ink-soft);
  }

  /* front side */
  .band {
    position: absolute; left: 0; right: 0; top: 52px; height: 178px;
    background: var(--band);
  }
  .person {
    position: absolute; left: 38px; top: 30px; width: 300px;
    font-family: "Montserrat", sans-serif; font-weight: 800;
    text-transform: uppercase; letter-spacing: 1px;
  }
  .person__name { font-size: 21px; }
  .person__degree { font-size: 12px; text-align: right; margin-top: 2px; }
  .person__role { font-size: 14px; margin-top: 10px; margin-left: 36px; }

  .address {
    position: absolute; right: 238px; top: 132px;
    text-align: right; font-size: 14px; line-height: 18px;
    text-transform: uppercase; letter-spacing: 0.6px; color: var(--ink-soft);
  }
  .divider {
    position: absolute; left: 310px; top: 130px; width: 1.5px; height: 62px;
    background: var(--rule);
  }
  .card--front .brand__name {
    position: absolute; left: 326px; top: 143px;
    font-weight: 500; font-size: 22px; letter-spacing: 2px;
    text-transform: uppercase; color: var(--ink);
  }
  .phones {
    position: absolute; right: 238px; top: 205px;
    text-align: right; font-size: 14px; line-height: 19px;
    letter-spacing: 0.8px; color: var(--ink-soft);
  }
  .online {
    position: absolute; left: 28px; right: 20px; bottom: 22px;
    font-size: 17px; line-height: 22px; letter-spacing: 0.6px;
    text-transform: uppercase; color: var(--ink-soft);
  }
  .online__web { padding-left: 24px; }
</style>
</head>
<body>
<main class="stage">
  <section class="card card--back" aria-label="Business card, back">
    <div class="brand">
      <span class="brand__name">Alpenvorsa</span>
      <span class="brand__rule"></span>
    </div>
    <p class="contact-email">m.dubrancq@alpenvorsa-example.com</p>
  </section>

  <section class="card card--front" aria-label="Business card, front">
    <div class="band"></div>
    <div class="person">
      <p class="person__name">Marisela Dubrancq</p>
      <p class="person__degree">M. Law</p>
      <p class="person__role">Managing Partner</p>
    </div>
    <address class="address" style="font-style:normal">
      Alpenvorsa AG<br>
      Kornhalmweg 214<br>
      CH-3097 Liebefeld
    </address>
    <span class="divider"></span>
    <span class="brand__name">Alpenvorsa</span>
    <p class="phones">
      M. +41 79 412 56 27<br>
      T. +41 31 928 44 10<br>
      F. +41 31 928 44 19
    </p>
    <p class="online">
      m.dubrancq@alpenvorsa-example.com<br>
      <span class="online__web">www.alpenvorsa-example.com</span>
    </p>
  </section>
</main>
</body>
</html>
```